Exciting New Reseller Brand requires Website to WOW New clients to register.

We are a NEW online business called Trade Our Goods.

The Website is a simple concept, it looks to put Merchants (businesses that want their products resold) in touch with Resellers (people or businesses that want to resell that product).

The website acts as an online market place which looks to get Merchants to sign-up and pay to list their company and product as well as getting Resellers to sign-up to view potential Merchants they can get in touch with in the right industry or area to resell their products for (see attached slide-pack to explain packages)

Any type of Industry or Business can register themselves to get listed on Trade Our Goods to see either get their product/service resold or to look for products / services to reseller.

Trade Our Goods does not take any other monetary part in the business relationships other than to obtain money for the monthly website subscription.

We want a very simple website, so this project is for several pages:

Page 1) A really vibrant, exciting, image based homepage to get people to sign-up / register (see sites that we like in the project brief). Needs to be very clear that there are 2 customers and to sign up to join, build and earn!

Page 2) A page that describes the benefits and packages for Resellers.

Page 3) A page that describes the benefits and packages for Merchants.

Page 4) The Payment process pages, taking the customer through sign-up

Page 5) The Business Listings page, so when people search for a Merchant how this will be displayed.

We would really like an image based site and preferably parallax. We want it bright vibrant and to look like a social media site.

All necessary files / logos enclosed.

We would love to continue to work with the winning designer moving forward.

Many thanks and Good Luck.

Regards

Martin & Owen

Target Market(s)

Merchants, Suppliers, Vendors, Manufacturers, Distributors, Wholesalers, Affiliate programs, Franchisees, Reselers

Industry/Entity Type

Business

Number of Pages Required

5+ page

Requirements
Must have
• We love the following websites:
• 1) Like the top section, i.e. parallax image based: www.brightkitestudio.co.uk
• 2) Like the way the screen is split in 2, could be used to describe the 2 different customers we are after Merchants / Resellers: www.filevault-example.com/guide
• 3) Like the bright colours / full screen video split into 2 below top banner and the generally how simple the site is: www.harbourlinden.com.au
• 4) Love all of this site, simple, bold, Love the colours, the clear message and the infographics: http://www.velorin-example.com/swiftrider/faster

```html
<!DOCTYPE html>
<html lang="en">
<head>
<meta charset="utf-8">
<title>Trade Our Goods — Building Your Own Virtual Sales Team</title>
<link rel="stylesheet" href="https://fonts.googleapis.com/css2?family=Open+Sans:wght@400;600;700;800&display=swap">
<style>
:root{
  --blue:#1b8fd8;
  --blue-dark:#1572b3;
  --green:#8dc63f;
  --green-dark:#6fa82a;
  --grey-hex:#9a9a9a;
  --ink:#333;
  --text:#555;
  --light:#f2f2f2;
  --dark:#2b2d31;
  --white:#fff;
}
*{box-sizing:border-box;margin:0;padding:0}
html,body{width:1200px;height:3939px;overflow:hidden}
body{font-family:"Open Sans",Arial,sans-serif;color:var(--text);background:var(--white);position:relative}
section,header,footer{position:relative;width:1200px;overflow:hidden}
ul{list-style:none}
.ticks li{position:relative;padding-left:36px}
.ticks li::before{content:"";position:absolute;left:6px;top:4px;width:8px;height:15px;border:solid var(--blue);border-width:0 4px 4px 0;transform:rotate(40deg)}
.ticks.green li::before{border-color:var(--green)}
.ticks.white li::before{border-color:var(--white)}
.lead{font-size:13px;font-weight:700;color:var(--ink);line-height:1.55;text-align:center;width:860px;margin:0 auto}

/* header */
.site-header{height:92px;background:var(--white)}
.brand{position:absolute;left:100px;top:14px;display:flex;align-items:center;gap:12px}
.brand-dot{width:54px;height:54px;border-radius:50%;background:var(--blue)}
.brand-name{font-size:34px;font-weight:700;color:var(--green-dark);letter-spacing:-.5px}
.social{position:absolute;right:96px;top:10px;display:flex;gap:6px}
.social span{width:22px;height:22px;border-radius:50%;background:#222;display:block}
.main-nav{position:absolute;right:58px;top:58px;display:flex;gap:34px;font-size:14px;color:var(--ink)}
.main-nav a{color:inherit;text-decoration:none;padding-bottom:12px}
.main-nav a.active{border-bottom:4px solid var(--green)}

/* hero */
.hero{height:562px;background:linear-gradient(90deg,#cfd3d6 0%,#e9ecee 35%,#f7f8f9 60%,#fff 100%)}
.hero-photo{position:absolute;left:0;top:0;width:560px;height:562px;background:linear-gradient(160deg,#d5d9dc,#b9bec2 60%,#8d9296)}
.hero-copy{position:absolute;right:102px;top:140px;text-align:right}
.hero-copy h1{font-size:48px;font-weight:700;color:var(--green);line-height:1.05}
.hero-copy h2{font-size:36px;font-weight:400;color:#444;line-height:1.3}
.hero-copy p{font-size:26px;color:#555;line-height:1.2}
.btn-blue{display:inline-block;margin-top:20px;background:var(--blue);color:var(--white);font-size:20px;padding:8px 20px}

/* intro split */
.intro{height:370px;display:flex}
.why{width:600px;background:var(--light);padding:26px 0 0 115px}
.why h2{font-size:34px;font-weight:800;color:var(--blue)}
.why h2 em{font-style:normal;color:var(--green)}
.why .sub{font-size:27px;color:#555;line-height:1.2;margin-top:6px}
.why .big{font-size:52px;font-weight:700;color:var(--ink);line-height:1.05}
.why .big em{font-style:normal;color:var(--green)}
.why ul{margin-top:14px;font-size:17px;line-height:31px}
.company{width:600px;background:var(--green);color:var(--white);padding:26px 0 0 36px}
.company h2{font-size:38px;font-weight:700}
.company .blurb{font-size:13px;font-weight:600;width:470px;line-height:1.5;margin-top:6px}
.company ul{margin-top:22px;font-size:18px;line-height:31px}

/* how it works */
.how{height:465px;text-align:center;padding-top:84px}
.section-title{font-size:36px;font-weight:400;color:var(--ink);margin-bottom:20px}
.steps{position:absolute;left:0;top:0;width:1200px;height:465px}
.step-label{position:absolute;top:360px;font-size:14px;color:var(--ink);width:140px;text-align:center}

/* pricing */
.pricing{height:420px}
.pricing.merchants{background:var(--light)}
.pricing.resellers{height:428px;background:var(--white)}
.price-copy{position:absolute}
.price-copy h3{font-size:34px;font-weight:400;color:#444;line-height:1.2}
.price-copy h2{font-size:50px;font-weight:800;line-height:1.05}
.price-copy ul{margin-top:34px;font-size:17px;line-height:37px;color:#444}
.merchants .price-copy{left:150px;top:42px}
.merchants .price-copy h2{color:var(--blue)}
.resellers .price-copy{left:643px;top:36px}
.resellers .price-copy h2{color:var(--green)}
.tier-table{position:absolute;border-collapse:collapse;table-layout:fixed;color:var(--white);font-weight:700}
.tier-table th{height:42px;font-size:18px;padding:0}
.tier-table tbody td{vertical-align:top;padding-top:8px;border-left:3px solid var(--white)}
.tier-table tbody td:first-child{border-left:none}
.tier-table tfoot td{height:36px;vertical-align:middle;padding:0;font-size:17px;text-align:center;border-left:3px solid var(--white)}
.tier-table tfoot td:first-child{border-left:none}
.tier-table small{font-size:9px;font-weight:400}
.tier-table .checks{display:flex;flex-direction:column;align-items:center}
.tier-table .checks i{display:block;width:10px;height:19px;border:solid;border-width:0 4px 4px 0;transform:rotate(40deg)}
.merchant-table{left:667px;top:60px;width:326px;border:3px solid var(--blue)}
.merchant-table th{background:var(--blue);border-left:3px solid var(--white)}
.merchant-table th:first-child{border-left:none}
.merchant-table tbody td{height:196px;background:var(--white);border-left-color:var(--blue)}
.merchant-table .checks{gap:15px}
.merchant-table .checks i{border-color:var(--green)}
.merchant-table tfoot td{background:var(--blue-dark)}
.reseller-table{left:184px;top:52px;width:331px;border:3px solid var(--green)}
.reseller-table th{background:var(--green);border-left:3px solid var(--white)}
.reseller-table th:first-child{border-left:none}
.reseller-table tbody td{height:165px;background:var(--white);border-left-color:var(--green)}
.reseller-table .checks{gap:13px}
.reseller-table .checks i{border-color:var(--green)}
.reseller-table tfoot td{background:var(--green-dark)}
.table-note{position:absolute;font-size:13px;color:#666}
.merchants .table-note{left:648px;top:372px}
.resellers .table-note{left:178px;top:362px}

/* benefits */
.benefits{height:473px;background:linear-gradient(90deg,#1f2124,#3b3e43 45%,#2a2c30);color:var(--white);text-align:center;padding-top:30px}
.benefits .section-title{color:var(--white);margin-bottom:8px}
.benefits .lead{color:var(--white)}
.benefit-card{position:absolute;top:163px;width:381px;background:var(--white);text-align:left}
.benefit-card h3{height:50px;line-height:50px;text-align:center;font-size:30px;font-weight:400;color:var(--white)}
.benefit-card ul{padding:16px 0 18px 24px;font-size:17px;line-height:35px;color:#444}
.benefit-card.merchant{left:147px}
.benefit-card.merchant h3{background:var(--blue)}
.benefit-card.reseller{left:662px}
.benefit-card.reseller h3{background:var(--green)}

/* clients */
.clients{height:533px;text-align:center;padding-top:44px}
.avatar{width:130px;height:130px;border-radius:50%;margin:20px auto 0;background:linear-gradient(160deg,#d9dcdf,#9ea3a8);border:5px solid #e6e6e6}
.quote{width:1060px;margin:24px auto 0;font-size:13px;line-height:1.9;color:var(--ink)}
.client-name{margin-top:22px;font-size:12px;font-weight:700;letter-spacing:2px;color:var(--ink)}
.client-company{font-size:13px;font-weight:700;color:var(--ink);margin-top:4px}
.slider-dots{display:flex;gap:6px;justify-content:center;margin-top:14px}
.slider-dots span{width:36px;height:7px;background:#c8c8c8}
.slider-dots span.on{background:var(--blue)}

/* quotes */
.quote-form{height:473px;background:linear-gradient(135deg,#1a86cf,#2a9be0 50%,#1577bd);text-align:center;padding-top:22px;color:var(--white)}
.quote-form .section-title{color:var(--white);margin-bottom:10px}
.quote-form .lead{color:var(--white)}
.field{position:absolute;left:215px;width:796px;border:2px solid rgba(255,255,255,.85);font-size:15px;font-style:italic;text-align:left;padding:0 14px;line-height:36px;color:var(--white)}
.field.name{top:144px;height:40px}
.field.email{top:206px;height:40px}
.field.message{top:262px;height:112px}
.btn-green{position:absolute;left:522px;top:399px;width:155px;height:47px;line-height:47px;background:var(--green);font-size:20px;font-weight:700;color:var(--white)}

/* footer */
.site-footer{height:123px;text-align:center}
.site-footer .social{position:static;justify-content:center;gap:8px;padding-top:30px}
.site-footer .social span{width:42px;height:42px}
.copyright{margin-top:14px;font-size:14px;color:var(--ink)}
</style>
</head>
<body>

<header class="site-header">
  <div class="brand"><span class="brand-dot"></span><span class="brand-name">Trade Our Goods</span></div>
  <div class="social"><span></span><span></span><span></span><span></span><span></span></div>
  <nav class="main-nav">
    <a href="#" class="active">Home</a><a href="#">About Us</a><a href="#">Services</a><a href="#">Our Work</a><a href="#">Products</a><a href="#">Contact</a>
  </nav>
</header>

<section class="hero">
  <div class="hero-photo" role="img" aria-label="Businessman seated at a desk working on a computer in a bright office"></div>
  <div class="hero-copy">
    <h1>BUILDING YOUR OWN</h1>
    <h2>VIRTUAL SALES TEAM</h2>
    <p>JOIN, BUILD, EARN</p>
    <span class="btn-blue">READMORE</span>
  </div>
</section>

<section class="intro">
  <div class="why">
    <h2>why <em>Pick</em> Reselling</h2>
    <p class="sub">Bringing reseller opportunities</p>
    <p class="big">to the <em>masses..</em></p>
    <ul class="ticks">
      <li>Personal requirement for a reseller base.</li>
      <li>Experienced reseller models that work.</li>
      <li>Building an effective virtual sales team.</li>
      <li>Helping SME's earn money for old rope.</li>
      <li>Easy to generate revenue for a minimal cost.</li>
    </ul>
  </div>
  <div class="company">
    <h2>Company Information</h2>
    <p class="blurb">Lorem Ipsum is simply dummy text of the printing and typesetting industry. Lorem Ipsum has been the industry's</p>
    <ul class="ticks white">
      <li>Portal for Resellers and Merchants.</li>
      <li>Merchants can promote their products.</li>
      <li>Merchants can build a virtual sales team.</li>
      <li>Resellers can expand product portfolio.</li>
      <li>Resellers can generate revenue.</li>
      <li>Industry news and opportunities.</li>
    </ul>
  </div>
</section>

<section class="how">
  <h2 class="section-title">How it Works</h2>
  <p class="lead">Lorem Ipsum is simply dummy text of the printing and typesetting industry. Lorem Ipsum has been the industry's standard dummy text ever since the 1500s, when an unknown printer took</p>
  <svg class="steps" viewBox="0 0 1200 465" aria-hidden="true">
    <defs>
      <path id="hex" d="M0,-56 L48.5,-28 L48.5,28 L0,56 L-48.5,28 L-48.5,-28 Z"/>
      <path id="arc" d="M0,0 Q27,-22 54,0" fill="none" stroke="#bbb" stroke-width="2"/>
    </defs>
    <g fill="#1b8fd8">
      <use href="#hex" x="150" y="286"/><use href="#hex" x="283" y="286"/><use href="#hex" x="412" y="286"/>
    </g>
    <g fill="#8dc63f">
      <use href="#hex" x="788" y="286"/><use href="#hex" x="919" y="286"/><use href="#hex" x="1050" y="286"/>
    </g>
    <path d="M604,190 L688,238 L688,334 L604,382 L520,334 L520,238 Z" fill="#9a9a9a"/>
    <text x="604" y="280" text-anchor="middle" fill="#fff" font-family="Open Sans, sans-serif" font-size="24" font-weight="700">PROMOTE</text>
    <text x="604" y="310" text-anchor="middle" fill="#fff" font-family="Open Sans, sans-serif" font-size="24" font-weight="700">AND EARN</text>
    <use href="#arc" x="190" y="230"/><use href="#arc" x="320" y="230"/><use href="#arc" x="450" y="230"/>
    <use href="#arc" x="690" y="230"/><use href="#arc" x="826" y="230"/><use href="#arc" x="956" y="230"/>
    <g fill="none" stroke="#fff" stroke-width="4" stroke-linecap="round">
      <circle cx="140" cy="273" r="6" fill="#fff"/><circle cx="160" cy="273" r="6" fill="#fff"/>
      <path d="M130,303 V289 h20 V303 M150,303 V289 h20 V303"/>
      <rect x="265" y="274" width="36" height="24" rx="3"/><path d="M265,282 h36"/>
      <rect x="397" y="268" width="30" height="36" rx="3"/><path d="M404,278 h16 M404,286 h16 M404,294 h10"/>
      <circle cx="784" cy="282" r="12"/><path d="M793,291 l10,10"/>
      <circle cx="914" cy="275" r="8"/><path d="M900,304 q14,-20 28,0 M932,282 v12 M926,288 h12"/>
      <circle cx="1050" cy="272" r="6" fill="#fff"/><circle cx="1036" cy="280" r="5" fill="#fff"/><circle cx="1064" cy="280" r="5" fill="#fff"/>
      <path d="M1040,302 q10,-18 20,0"/>
    </g>
  </svg>
  <span class="step-label" style="left:80px">Merchants</span>
  <span class="step-label" style="left:213px">Payment</span>
  <span class="step-label" style="left:342px">Listing</span>
  <span class="step-label" style="left:718px">Search</span>
  <span class="step-label" style="left:849px">Register</span>
  <span class="step-label" style="left:980px">Resellers</span>
</section>

<section class="pricing merchants">
  <div class="price-copy">
    <h3>Product Price Structure</h3>
    <h2>MERCHANTS</h2>
    <ul class="ticks">
      <li>Directory Listing</li>
      <li>Monthly Newsletters</li>
      <li>Seminars &amp; Network Events</li>
      <li>Onsite Advertising</li>
      <li>Dedicated Reseller Scout</li>
    </ul>
  </div>
  <table class="tier-table merchant-table">
    <thead><tr><th>Tier 1</th><th>Tier 2</th><th>Tier 3</th></tr></thead>
    <tbody><tr>
      <td><div class="checks"><i></i></div></td>
      <td><div class="checks"><i></i><i></i><i></i></div></td>
      <td><div class="checks"><i></i><i></i><i></i><i></i><i></i></div></td>
    </tr></tbody>
    <tfoot><tr><td>£50 <small>p/month</small></td><td>£150 <small>p/month</small></td><td>£300 <small>p/month</small></td></tr></tfoot>
  </table>
  <p class="table-note">All are minimum of 12 months, discounts for 24 months.</p>
</section>

<section class="pricing resellers">
  <table class="tier-table reseller-table">
    <thead><tr><th>Tier 1</th><th>Tier 2</th><th>Tier 3</th></tr></thead>
    <tbody><tr>
      <td><div class="checks"><i></i></div></td>
      <td><div class="checks"><i></i><i></i><i></i></div></td>
      <td><div class="checks"><i></i><i></i><i></i><i></i><i></i></div></td>
    </tr></tbody>
    <tfoot><tr><td>FREE</td><td>£25 <small>p/month</small></td><td>£100 <small>p/month</small></td></tr></tfoot>
  </table>
  <p class="table-note">All are minimum of 12 months, discounts for 24 months.</p>
  <div class="price-copy">
    <h3>Product Price Structure</h3>
    <h2>RESELLERS</h2>
    <ul class="ticks green">
      <li>Search Merchant Database</li>
      <li>Reseller Listing</li>
      <li>Monthly Newsletters</li>
      <li>Seminars &amp; Network Events</li>
      <li>Dedicated Merchant Scout</li>
    </ul>
  </div>
</section>

<section class="benefits" role="img" aria-label="Dark background photo of people working at laptops">
  <h2 class="section-title">Benefits For Everyone</h2>
  <p class="lead">Lorem Ipsum is simply dummy text of the printing and typesetting industry. Lorem Ipsum has been the industry's standard dummy text ever since the 1500s, when an unknown printer took</p>
  <div class="benefit-card merchant">
    <h3>Merchants</h3>
    <ul class="ticks">
      <li>Additional Source of Sales</li>
      <li>Incremental Growth</li>
      <li>Viral Brand Recognition</li>
      <li>Virtual Sales Team</li>
      <li>No Overheads</li>
    </ul>
  </div>
  <div class="benefit-card reseller">
    <h3>Resellers</h3>
    <ul class="ticks">
      <li>Additional Stream of Income</li>
      <li>Infrastructure in Place</li>
      <li>No Additional Cost</li>
      <li>Expand Product Suite</li>
      <li>Reach New Target Markets</li>
    </ul>
  </div>
</section>

<section class="clients">
  <h2 class="section-title" style="margin-bottom:12px">Our Clientes</h2>
  <p class="lead">Lorem Ipsum is simply dummy text of the printing and typesetting industry. Lorem Ipsum has been the industry's standard dummy text ever since the 1500s, when an unknown printer took</p>
  <div class="avatar" role="img" aria-label="Portrait photo of the client"></div>
  <p class="quote">A wonderful serenity has taken possession of my entire soul, like these sweet mornings of spring which I enjoy with my whole heartle heart. I am alone, and feel the charm of existence in this spot, which was created for the I am alone, and feel the charm of existence in this spot, which was created for the bliss of souls like mine. I am so happy.</p>
  <p class="client-name">SAM CARTER</p>
  <p class="client-company">Brightline Supply Co</p>
  <div class="slider-dots"><span class="on"></span><span></span><span></span><span></span><span></span></div>
</section>

<section class="quote-form" role="img" aria-label="Blue tinted photo of a person typing on a laptop">
  <h2 class="section-title">Free Quotes</h2>
  <p class="lead">Lorem Ipsum is simply dummy text of the printing and typesetting industry. Lorem Ipsum has been the industry's standard dummy text ever since the 1500s, when an unknown printer took</p>
  <div class="field name">Enter Name</div>
  <div class="field email">Enter Email</div>
  <div class="field message"></div>
  <div class="btn-green">Submit Now</div>
</section>

<footer class="site-footer">
  <div class="social"><span></span><span></span><span></span><span></span><span></span></div>
  <p class="copyright">© 2010 Tradeourgoods.com . All Rights Reserved</p>
</footer>

</body>
</html>
```